Business cards — need something that creates “wow” factor

Need a sleek and clean looking business card. Something that is clear and consise. These business cards are for my painting business and hundreds will be placed in the Dallas area between all Halverd Pemberton paint stored. These card really need to stick out! Open to any and all ideas...

Target Market(s)

Residential clientele

Industry/Entity Type

Painting

Contact Information for Business Card

Dorian Vakelby
Owner

382.516.2074

Web: Mesahuepainting.example (still under construction)
Mesahuepainting@mailbox.example

Font styles to use
Sans Serif

Colors

Designer to choose colors to be used in the design.

Requirements
Must have
• My name, number, website, email, Socialpage
• and “100% customer satisfaction guaranteed”
• Socialpage.example/Mesahuepainting/
Nice to have
• Listed services
• Interior/exterior painting
• Drywall repair/texture
• Fence staining/refinishing
• Concrete staining
• Epoxy flooring
• Pressure washing

```html
<!DOCTYPE html>
<html lang="en">
<head>
<meta charset="utf-8">
<title>Mesahue Painting — Business Cards</title>
<link href="https://fonts.googleapis.com/css2?family=Raleway:wght@300;400;500;700&display=swap" rel="stylesheet">
<style>
  :root {
    --backdrop: #e9e7e4;
    --card-white: #ffffff;
    --ink: #141414;
    --panel-black: #151515;
    --band-yellow: #f7bd10;
    --muted: #555555;
    --shadow: rgba(0,0,0,0.22);
  }
  * { margin: 0; padding: 0; box-sizing: border-box; }
  html, body {
    width: 1200px; height: 950px; overflow: hidden;
    background: var(--backdrop);
    font-family: "Raleway", sans-serif;
    color: var(--ink);
  }
  .canvas { position: relative; width: 1200px; height: 950px; }

  .card {
    position: absolute;
    width: 700px; height: 400px;
    background: var(--card-white);
    box-shadow: 0 14px 30px var(--shadow);
    overflow: hidden;
  }

  /* Front */
  .card-front { left: 420px; top: 50px; }
  .brand {
    position: absolute; left: 0; right: 0; top: 130px;
    text-align: center;
  }
  .brand-name {
    font-size: 62px; font-weight: 500; letter-spacing: 2px;
    color: var(--ink); line-height: 1;
  }
  .brand-tagline {
    margin-top: 18px;
    font-size: 15px; font-weight: 400; color: var(--muted);
    letter-spacing: 0.5px;
  }
  .brand-tagline .sep { color: #4a8fc9; margin: 0 6px; }

  /* Back */
  .card-back { left: 90px; top: 490px; }
  .back-shapes { position: absolute; inset: 0; }
  .identity { position: absolute; left: 42px; top: 58px; width: 330px; }
  .person-name { font-size: 40px; line-height: 1; white-space: nowrap; }
  .person-name .first { font-weight: 700; }
  .person-name .last { font-weight: 400; }
  .person-role { font-size: 21px; font-weight: 300; margin-top: 6px; }
  .rule { height: 2px; background: var(--ink); margin: 16px 0 22px; width: 330px; }
  .contact-list { list-style: none; }
  .contact-item {
    display: flex; align-items: center; gap: 14px;
    font-size: 17px; font-weight: 500; margin-bottom: 12px; white-space: nowrap;
  }
  .contact-item svg { width: 22px; height: 22px; flex: none; }

  .services {
    position: absolute; left: 420px; top: 120px;
    list-style: none; color: #fff;
  }
  .services li {
    font-size: 18px; font-weight: 400; margin-bottom: 6px;
    padding-left: 20px; position: relative;
  }
  .services li::before {
    content: ""; position: absolute; left: 0; top: 9px;
    width: 6px; height: 6px; border-radius: 50%; background: #fff;
  }
  .guarantee {
    position: absolute; left: 360px; right: 0; bottom: 14px;
    text-align: center; font-size: 18px; font-weight: 500; color: var(--ink);
  }
</style>
</head>
<body>
<main class="canvas">
  <section class="card card-front" aria-label="Card front">
    <div class="brand">
      <div class="brand-name">Mesahue Painting</div>
      <div class="brand-tagline">Commercial<span class="sep">|</span>Residential<span class="sep">|</span>Interior<span class="sep">|</span>Exterior</div>
    </div>
  </section>

  <section class="card card-back" aria-label="Card back">
    <svg class="back-shapes" viewBox="0 0 700 400" preserveAspectRatio="none" aria-hidden="true">
      <path d="M345 0 C 420 110, 420 270, 330 400 L700 400 L700 0 Z" fill="var(--panel-black)"/>
      <path d="M360 400 C 360 370, 380 345, 420 345 L700 345 L700 400 Z" fill="var(--band-yellow)"/>
    </svg>

    <div class="identity">
      <div class="person-name"><span class="first">Dorian</span> <span class="last">Vakelby</span></div>
      <div class="person-role">Owner</div>
      <div class="rule"></div>
      <ul class="contact-list">
        <li class="contact-item">
          <svg viewBox="0 0 24 24" aria-hidden="true"><circle cx="12" cy="12" r="10.5" fill="none" stroke="currentColor" stroke-width="1.6"/><path d="M9 7.5c-1 .8-1.3 2-.8 3.5.8 2.3 2.3 4 4.3 5 .9.4 1.7.3 2.3-.4l.6-.7-1.8-1.5-.9.7c-1-.5-1.8-1.4-2.2-2.5l.8-.8-1.2-2z" fill="currentColor"/></svg>
          382.516.2074
        </li>
        <li class="contact-item">
          <svg viewBox="0 0 24 24" aria-hidden="true"><rect x="2" y="5" width="20" height="14" fill="currentColor"/><path d="M2 5l10 8 10-8" fill="none" stroke="#fff" stroke-width="1.6"/></svg>
          Mesahuepainting@mailbox.example
        </li>
        <li class="contact-item">
          <svg viewBox="0 0 24 24" aria-hidden="true" fill="none" stroke="currentColor" stroke-width="1.4"><circle cx="12" cy="12" r="10"/><ellipse cx="12" cy="12" rx="4.5" ry="10"/><path d="M2 12h20M4 7h16M4 17h16"/></svg>
          www.Mesahuepainting.example
        </li>
      </ul>
    </div>

    <ul class="services">
      <li>Interior/exterior painting</li>
      <li>Drywall repair/texture</li>
      <li>Fence staining/refinishing</li>
      <li>Concrete staining</li>
      <li>Epoxy flooring</li>
      <li>Pressure washing</li>
    </ul>

    <div class="guarantee">100% customer satisfaction guaranteed</div>
  </section>
</main>
</body>
</html>
```